" A EMPRESA ATUA NO SEGMENTO DE OUTSOURCING DE PrintoraÃO: LOCAÇÃO DE IMPRESSORAS E MULTIFUNCIONAIS, E IMPLANTAÇÃO DE SOFTWARES AGREGADOS A ESSAS MÁQUINAS. "

```html
<!DOCTYPE html>
<html lang="pt-BR">
<head>
<meta charset="UTF-8">
<title>Printora – Papel timbrado</title>
<link href="https://fonts.googleapis.com/css2?family=Montserrat:wght@400;600;700&family=Open+Sans:wght@400;600&display=swap" rel="stylesheet">
<style>
  :root {
    --navy: #1f2a5c;
    --navy-soft: #3a4678;
    --grey-band: #7d8294;
    --text: #4a4d57;
    --faint: #eceef3;
    --backdrop: #e6e7ea;
    --paper: #ffffff;
  }
  * { margin: 0; padding: 0; box-sizing: border-box; }
  html, body {
    width: 1200px; height: 1200px; overflow: hidden;
    background: var(--backdrop);
  }
  .letterhead {
    position: absolute; left: 220px; top: 40px;
    width: 760px; height: 1120px;
    background: var(--paper);
    box-shadow: 0 6px 30px rgba(0,0,0,0.12);
    overflow: hidden;
  }
  .backdrop-mark {
    position: absolute; left: 150px; top: 300px;
    width: 400px; height: 480px;
    border: 46px solid var(--faint);
  }
  .brand {
    position: absolute; right: 70px; top: 70px;
    display: flex; align-items: center; gap: 14px;
  }
  .brand-square {
    width: 34px; height: 34px; background: var(--navy);
  }
  .brand-text { display: flex; flex-direction: column; }
  .brand-name {
    font-family: "Montserrat", sans-serif; font-weight: 700;
    font-size: 38px; letter-spacing: 2px; color: var(--navy); line-height: 1;
  }
  .brand-tagline {
    font-family: "Montserrat", sans-serif; font-weight: 600;
    font-size: 11px; letter-spacing: 2px; color: var(--navy-soft);
    margin-top: 5px; text-transform: uppercase;
  }
  .letter-body {
    position: absolute; left: 80px; right: 80px; top: 200px;
    font-family: "Open Sans", sans-serif; font-size: 16px;
    line-height: 1.9; color: var(--text); text-align: justify;
  }
  .letter-body p { margin-bottom: 22px; }
  .footer-bands {
    position: absolute; left: 0; bottom: 0; width: 760px; height: 200px;
  }
  .contacts {
    position: absolute; left: 80px; bottom: 120px;
    display: grid; grid-template-columns: 260px 300px; row-gap: 14px; column-gap: 40px;
    font-family: "Open Sans", sans-serif; font-size: 13px; color: var(--text);
  }
  .contact-item { display: flex; align-items: center; gap: 10px; }
  .contact-icon {
    width: 22px; height: 22px; background: var(--navy);
    display: flex; align-items: center; justify-content: center; flex: none;
  }
</style>
</head>
<body>
  <main class="letterhead">
    <div class="backdrop-mark"></div>

    <header class="brand">
      <div class="brand-square"></div>
      <div class="brand-text">
        <span class="brand-name">PRINTORA</span>
        <span class="brand-tagline">Outsourcing de impressão</span>
      </div>
    </header>

    <section class="letter-body">
      <p>Prezado cliente, agradecemos a confiança em nossos serviços de locação de impressoras e multifuncionais. Nossa equipe acompanha cada contrato de perto, garantindo manutenção preventiva, suprimentos entregues no prazo e suporte técnico ágil sempre que necessário.</p>
      <p>Com a implantação de softwares de gestão de impressão, sua empresa passa a controlar custos por usuário e por setor, reduz desperdícios de papel e toner e obtém relatórios claros para decisões mais seguras no dia a dia.</p>
      <p>Permanecemos à disposição para apresentar uma proposta sob medida, alinhada ao volume de impressão e às necessidades de cada área da sua organização.</p>
      <p>Atenciosamente, equipe comercial.</p>
    </section>

    <section class="contacts">
      <div class="contact-item">
        <span class="contact-icon"><svg width="12" height="12" viewBox="0 0 24 24"><path fill="#fff" d="M6.6 10.8a15 15 0 0 0 6.6 6.6l2.2-2.2c.3-.3.7-.4 1-.2 1.1.4 2.3.6 3.6.6.6 0 1 .4 1 1V20c0 .6-.4 1-1 1A17 17 0 0 1 3 4c0-.6.4-1 1-1h3.5c.6 0 1 .4 1 1 0 1.3.2 2.5.6 3.6.1.3 0 .7-.2 1z"/></svg></span>
        (11) 5550-0123
      </div>
      <div class="contact-item">
        <span class="contact-icon"><svg width="12" height="12" viewBox="0 0 24 24"><circle cx="12" cy="12" r="9" fill="none" stroke="#fff" stroke-width="2"/><path d="M3 12h18M12 3c3 3 3 15 0 18M12 3c-3 3-3 15 0 18" fill="none" stroke="#fff" stroke-width="1.6"/></svg></span>
        www.printora.com.br
      </div>
      <div class="contact-item">
        <span class="contact-icon"><svg width="12" height="12" viewBox="0 0 24 24"><rect x="3" y="5" width="18" height="14" fill="none" stroke="#fff" stroke-width="2"/><path d="M3 6l9 7 9-7" fill="none" stroke="#fff" stroke-width="2"/></svg></span>
        contato@printora.com.br
      </div>
      <div class="contact-item">
        <span class="contact-icon"><svg width="12" height="12" viewBox="0 0 24 24"><path fill="#fff" d="M12 2a7 7 0 0 0-7 7c0 5 7 13 7 13s7-8 7-13a7 7 0 0 0-7-7zm0 9.5A2.5 2.5 0 1 1 12 6.5a2.5 2.5 0 0 1 0 5z"/></svg></span>
        Rua das Acácias, 120 – São Paulo – SP
      </div>
    </section>

    <svg class="footer-bands" viewBox="0 0 760 200" aria-hidden="true">
      <polygon points="0,150 520,150 560,176 0,176" fill="var(--navy)"/>
      <polygon points="0,186 560,186 575,196 0,196" fill="var(--grey-band)"/>
    </svg>
  </main>
</body>
</html>
```